The Kestrel Personal Training Studio Information Card

The front and back of card to give people that walk in to our gym. There are a few things to say on the card. But it also needs to be designed in an attractive way. You can make some of the information bullett points or with icons or graphics. Please look at our website at https://thekestrelfitness-example.com/ . The card will be 4" x 9"

Target Market(s)

High End Clientele who want to train in a private gym

Industry/Entity Type

Fitness

Font styles to use
Serif
Sans Serif
Other font styles liked:
• the same font Vorlex uses on the zuntab

Colors
F0912C
F2A743
F7CA91
FBE8D2
FDF5EE

Requirements
Must have
• A cool look

```html
<!DOCTYPE html>
<html lang="en">
<head>
<meta charset="utf-8">
<title>The Kestrel Personal Training Studio – Information Card</title>
<link href="https://fonts.googleapis.com/css2?family=Inter:wght@400;500;700;800&display=swap" rel="stylesheet">
<style>
  :root{
    --orange:#ee6834;
    --white:#ffffff;
    --ink:#4a4a4a;
    --photo-dark:#22252a;
    --photo-mid:#3b4038;
    --photo-green:#4d7a2c;
    --page:#ffffff;
  }
  *{margin:0;padding:0;box-sizing:border-box}
  html,body{width:1200px;height:1200px;overflow:hidden;background:var(--page)}
  body{font-family:"Inter",Arial,sans-serif;color:var(--white);position:relative}

  .card{position:absolute;left:111px;width:980px;height:435px;overflow:hidden}
  .card--front{top:123px}
  .card--back{top:614px}

  /* front */
  .front-photo{position:absolute;left:0;top:0;width:656px;height:435px;
    background:linear-gradient(160deg,#4a4f55 0%,var(--photo-dark) 45%,#2c3a22 75%,#1c1e21 100%)}
  .front-headline{position:absolute;left:36px;top:323px;font-size:30.5px;line-height:39px;letter-spacing:-.3px}
  .front-headline .accent{color:var(--orange);font-weight:700;display:block}
  .front-headline .plain{color:var(--white);font-weight:400;display:block}

  .info-panel{position:absolute;left:656px;top:0;width:324px;height:435px;background:var(--orange);padding:0 20px 0 26px}
  .brand{margin-top:28px;text-align:center;font-weight:800;font-size:34px;letter-spacing:1px;color:var(--ink);line-height:1}
  .brand-sub{text-align:center;font-size:9.5px;font-weight:700;letter-spacing:4.2px;color:var(--ink);margin-top:6px}
  .goals-title{margin-top:22px;font-size:16.5px;font-weight:700;letter-spacing:-.2px}
  .goals{list-style:none;font-size:13.4px;line-height:19.6px;margin-top:2px}
  .goals li::before{content:"";display:inline-block;width:5px;height:5px;border-radius:50%;background:var(--white);margin-right:7px;vertical-align:-1px}
  .info-panel p{font-size:13.4px;line-height:19.6px}
  .info-panel p + p{margin-top:11px}

  /* back */
  .back-photo{position:absolute;inset:0;
    background:linear-gradient(180deg,#2a2220 0%,#3d3230 40%,#2e3a24 80%,#3c4a28 100%)}
  .brush{position:absolute;left:0;top:0}
  .rates-title{position:absolute;left:59px;top:25px;font-size:41px;font-weight:700;color:var(--orange);letter-spacing:-.5px}
  .rates-sub{position:absolute;left:92px;top:80px;font-size:32px;color:var(--orange);letter-spacing:-.3px}
  .rate{position:absolute;top:131px;width:151px;height:150px;border-radius:18px;background:var(--orange);text-align:center;padding-top:16px}
  .rate:nth-of-type(1){left:44px}
  .rate:nth-of-type(2){left:215px}
  .rate:nth-of-type(3){left:388px}
  .rate-freq{font-size:19.5px;line-height:24px}
  .rate-price{font-size:43px;font-weight:800;line-height:50px;letter-spacing:-.5px}
  .rate-unit{font-size:19.5px;line-height:22px}
  .partner{position:absolute;left:0;width:560px;top:333px;text-align:center;font-size:22px;font-weight:700;letter-spacing:-.3px}
  .partner .accent{color:var(--orange)}
  .partner-note{position:absolute;left:40px;width:520px;top:370px;text-align:center;font-size:14.6px;line-height:20px}
  .start-title{position:absolute;left:608px;top:50px;width:340px;font-size:36.5px;line-height:45px;font-weight:700;letter-spacing:-.4px}
  .start-copy{position:absolute;left:608px;top:146px;width:355px;font-size:19.6px;line-height:27.2px;letter-spacing:-.2px}
</style>
</head>
<body>

<section class="card card--front">
  <div class="front-photo" role="img" aria-label="Photo of a trainer spotting a woman doing a barbell back squat in a gym with green racks"></div>
  <h1 class="front-headline">
    <span class="accent">A SAFE AND INDIVIDUALIZED</span>
    <span class="plain">APPROACH TO STRENGTH TRAINING.</span>
  </h1>
  <div class="info-panel">
    <div class="brand">THE KESTREL</div>
    <div class="brand-sub">PRIVATE TRAINING STUDIO</div>
    <h2 class="goals-title">Our clients have different goals:</h2>
    <ul class="goals">
      <li>Build strength,</li>
      <li>Increase Flexibility,</li>
      <li>Improve functional and daily movements,</li>
      <li>Train for an event, or</li>
      <li>Weight Loss.</li>
    </ul>
    <p>We will tailor your training program to the specific results you are looking for.</p>
    <p>Some ways of training increase the chance of injury, we do not practice those types of training at The Kestrel. Many of our clients have current or past injuries that can cause problems. We work with them to not aggravate those injuries or allow them to become an obstacle to their workouts.</p>
  </div>
</section>

<section class="card card--back">
  <div class="back-photo" role="img" aria-label="Photo of a man training on a rowing machine in a gym"></div>
  <svg class="brush" width="980" height="435" viewBox="0 0 980 435" aria-hidden="true">
    <path d="M690 0 L980 0 L980 435 L640 435 L610 400 L560 360 L600 330 L580 300 L640 260 L600 220 L650 180 L620 140 L670 100 L640 60 Z" fill="var(--orange)"/>
  </svg>

  <h2 class="rates-title">Our Rates:</h2>
  <div class="rates-sub">All Sessions are 60 minutes</div>

  <div class="rate">
    <div class="rate-freq">1 time per<br>week:</div>
    <div class="rate-price">$110</div>
    <div class="rate-unit">per session</div>
  </div>
  <div class="rate">
    <div class="rate-freq">2 times per<br>week:</div>
    <div class="rate-price">$85</div>
    <div class="rate-unit">per session</div>
  </div>
  <div class="rate">
    <div class="rate-freq">3 times per<br>week</div>
    <div class="rate-price">$80</div>
    <div class="rate-unit">per session</div>
  </div>

  <div class="partner"><span class="accent">Add $40</span> for a Partnered Session</div>
  <p class="partner-note">Example: A Partnered Session (2 people training together) coming twice a week is $125 per session</p>

  <h2 class="start-title">How do you get started?</h2>
  <p class="start-copy">We schedule prospective clients for a no cost or obligation consultation. At that consultation we will do a movement screen with you. This will allow the trainer to see what level of flexibility and strength you are currently at. You will be able to discuss your goals and other issues (injuries, etc) at that time.</p>
</section>

</body>
</html>
```